I am looking for a stand-out cover that sings out to new parents. The category is very pastel with limited compelling covers that would make me want to buy a book. This book will be used often in the first 12 months of baby's life - so must be strong enough to sit on the bedside table or on the coffee table to inspire reading. It will be a popular gift - so needs to look credible, "pick-up-able" and loveable.

The Book Title is - The Cradle Compass to Infancy's Opening Seasons: Grounded, Research-Led Methods on Rest, Nourishment, Protection plus Growing Assurance
The Size is - 8.5 x 11 in
Book description to be provided to final design for inclusion
Some examples of book covers in this category attached. Thanks

```html
<!DOCTYPE html>
<html lang="en">
<head>
<meta charset="utf-8">
<title>The Cradle Compass to Infancy's Opening Seasons</title>
<link href="https://fonts.googleapis.com/css2?family=Cinzel:wght@500;600&family=Great+Vibes&family=Domine:wght@400;500;600&display=swap" rel="stylesheet">
<style>
  :root {
    --backdrop: #e4e8e9;
    --paper: #fdf8ec;
    --ink: #1c2b3a;
    --rule: #2a3d4e;
    --gold: #b48a2c;
    --green: #2f5a3e;
    --sage: #d6dbcf;
    --blush: #eee5d3;
    --mist: #dfe3dc;
  }
  * { margin: 0; padding: 0; box-sizing: border-box; }
  html, body {
    width: 1200px;
    height: 1164px;
    overflow: hidden;
    background: var(--backdrop);
  }
  .cover {
    position: absolute;
    left: 182px;
    top: 42px;
    width: 836px;
    height: 1080px;
    background: var(--paper);
    color: var(--ink);
    text-align: center;
  }
  .title-main {
    position: absolute;
    top: 72px;
    left: 0;
    width: 100%;
    font-family: "Cinzel", serif;
    font-weight: 600;
    font-size: 74px;
    line-height: 78px;
    letter-spacing: 1px;
    background: linear-gradient(100deg, var(--gold) 0%, var(--green) 22%, var(--gold) 40%, var(--green) 60%, var(--gold) 78%, var(--green) 100%);
    -webkit-background-clip: text;
    background-clip: text;
    color: transparent;
  }
  .title-joiner {
    position: absolute;
    top: 228px;
    left: 0;
    width: 100%;
    display: flex;
    align-items: center;
    justify-content: center;
    gap: 18px;
    font-family: "Cinzel", serif;
    font-weight: 500;
    font-size: 36px;
    color: var(--gold);
  }
  .title-joiner .rule {
    width: 175px;
    height: 2px;
    background: var(--rule);
  }
  .title-script {
    position: absolute;
    top: 298px;
    left: 0;
    width: 100%;
    font-family: "Great Vibes", cursive;
    font-size: 78px;
    line-height: 96px;
    color: var(--ink);
  }
  .cover-art {
    position: absolute;
    left: 122px;
    top: 440px;
    width: 592px;
    height: 400px;
    border-radius: 14px;
    background: linear-gradient(135deg, var(--mist) 0%, var(--sage) 45%, var(--blush) 100%);
  }
  .subtitle {
    position: absolute;
    top: 900px;
    left: 60px;
    width: 716px;
    font-family: "Domine", serif;
    font-weight: 500;
    font-size: 25px;
    line-height: 35px;
    color: var(--ink);
  }
  .author {
    position: absolute;
    top: 1018px;
    left: 0;
    width: 100%;
    font-family: "Domine", serif;
    font-weight: 600;
    font-size: 27px;
    letter-spacing: 0.5px;
    color: var(--ink);
  }
</style>
</head>
<body>
  <main class="cover">
    <h1 class="title-main">THE CRADLE<br>COMPASS</h1>
    <div class="title-joiner"><span class="rule"></span>TO<span class="rule"></span></div>
    <p class="title-script">Infancy's Opening Seasons</p>
    <div class="cover-art" role="img" aria-label="Fine line drawing of a parent's hand cradling a baby's foot, framed by delicate wildflowers and leaves"></div>
    <p class="subtitle">Grounded, Research-Led Methods on Rest, Nourishment, Protection plus Growing Assurance</p>
    <p class="author">AUTHOR NAME</p>
  </main>
</body>
</html>
```